Business Card and Letterhead for Nurlo - modern real estate business

I need a double sided business card design for Nurlo. Please see business card brief here https://papers.trelvimo.net/sheet/q/7XrTbaLeZpMmQ2uWvd9HkCj4yNoEfsGi3lRtAz_pk/view?mode=shared

Please feel free to design the business cards however you feel best. I am happy to give some creative freedoms and then provide feedback from there.

Please then also create a letterhead to match the business card design

Colors

Designer to choose colors to be used in the design.

Requirements
Must have
• Must be a modern, elegant business card which looks very professional

```html
<!DOCTYPE html>
<html lang="en">
<head>
<meta charset="utf-8">
<title>Nurlo Business Card</title>
<link href="https://fonts.googleapis.com/css2?family=Crimson+Pro:wght@400;600&display=swap" rel="stylesheet">
<style>
  :root {
    --page-bg: #e9e9e9;
    --card-dark: #231f20;
    --card-light: #ffffff;
    --brand-red: #e31e24;
    --text-grey: #5a5a5a;
    --photo-light: #d9d6d3;
    --photo-dark: #2a2a2c;
  }
  * { margin: 0; padding: 0; box-sizing: border-box; }
  html, body {
    width: 1200px; height: 801px; overflow: hidden;
    background: var(--page-bg);
    font-family: "Crimson Pro", Georgia, serif;
  }
  .card {
    position: absolute; left: 327px;
    width: 546px; height: 333px;
    border-radius: 13px; overflow: hidden;
  }
  .card--front { top: 62px; background: var(--card-dark); }
  .card--back { top: 429px; background: var(--card-light); }

  .brand-name {
    position: absolute; color: var(--brand-red);
    font-weight: 600; text-transform: uppercase; line-height: 1;
    letter-spacing: 0.04em;
  }
  .card--front .brand-name {
    left: 0; right: 0; top: 124px;
    text-align: center; font-size: 88px;
  }
  .card--back .brand-name {
    left: 23px; top: 48px; font-size: 48px;
  }

  .agent-name {
    position: absolute; left: 23px; top: 141px;
    font-size: 25px; font-weight: 600; color: var(--brand-red);
    letter-spacing: 0.02em;
  }
  .agent-role {
    position: absolute; left: 23px; top: 170px;
    font-size: 15px; color: var(--text-grey);
  }
  .divider {
    position: absolute; left: 23px; top: 196px;
    width: 9px; height: 2px; background: var(--brand-red);
  }
  .contact-list { position: absolute; left: 23px; top: 206px; list-style: none; }
  .contact-item {
    display: flex; align-items: center; height: 20.5px;
    font-size: 14.5px; color: var(--text-grey);
  }
  .contact-icon { width: 10px; height: 10px; margin-right: 7px; flex: none; }

  .address-band {
    position: absolute; left: 0; top: 284px;
    width: 265px; height: 35px; background: var(--brand-red);
    color: #fff; font-size: 13.5px;
    display: flex; align-items: center; padding-left: 23px;
  }
  .agent-photo {
    position: absolute; left: 260px; top: 15px;
    width: 286px; height: 318px;
    background: linear-gradient(180deg, var(--photo-light) 0%, #b89a86 30%, var(--photo-dark) 55%, var(--photo-dark) 100%);
    border-radius: 120px 120px 0 0;
  }
</style>
</head>
<body>
  <section class="card card--front">
    <div class="brand-name">Nurlo</div>
  </section>

  <section class="card card--back">
    <div class="brand-name">Nurlo</div>
    <div class="agent-name">Liam Porter</div>
    <div class="agent-role">Licenced Real Estate Agent</div>
    <div class="divider"></div>
    <ul class="contact-list">
      <li class="contact-item">
        <svg class="contact-icon" viewBox="0 0 10 10"><path d="M2 0.5 L3.8 2.6 L2.9 3.6 Q3.8 5.6 6.4 7.1 L7.4 6.2 L9.5 8 L8.2 9.5 Q3.6 8.8 0.5 2 Z" fill="#e31e24"/></svg>
        0412 555 318
      </li>
      <li class="contact-item">
        <svg class="contact-icon" viewBox="0 0 10 10"><rect x="0.5" y="1.5" width="9" height="7" fill="#e31e24"/><path d="M1.5 2.5 L5 5.5 L8.5 2.5" stroke="#fff" stroke-width="1" fill="none"/></svg>
        liam@nurlo.com
      </li>
      <li class="contact-item">
        <svg class="contact-icon" viewBox="0 0 10 10"><circle cx="5" cy="5" r="4.5" fill="#e31e24"/><path d="M2.5 3 Q4 2.5 4.5 4 Q3.5 5.5 4.2 7 M6.5 2 Q7.5 4 6.2 5.5 Q7 7 8 7" stroke="#fff" stroke-width="0.9" fill="none"/></svg>
        www.nurlo.com
      </li>
    </ul>
    <div class="address-band">PO Box 3170 Ferndale NSW 2790</div>
    <div class="agent-photo" role="img" aria-label="Portrait photo of the agent in a dark suit"></div>
  </section>
</body>
</html>
```